Golf Tournament Raffle

I need a promotional flyer for 1 week family vaction in Mexico. The week includes a stay at the Calloway Resort, a 5 star hotel. Id like the flyer to have images of a family at the beach, kids playing in pool, and images of drinks and food. It doesnt have to be all these images, but whomever looks at the flyer should automatically be inspired to take a family vaction. The vacation will be given away at our annual golf tournament hosted by Holy Meadow Of Brenton Catholic School. The way to enter the cobtest is to purchase as many golf balls for $50.00. All golf balls will be dropped from a helicopter and the ball that falls inside a hole wins the vacation, this is called a "Ball Drop" the main focal point is the Vacation. I will add the logo of the tournament and thr logo of the school hosting the tournament. The date of the tournament is November 11th and you dont need to be present to win

```html
<!DOCTYPE html>
<html lang="en">
<head>
<meta charset="utf-8">
<title>Golf Tournament Ball Drop Flyer</title>
<link rel="stylesheet" href="https://fonts.googleapis.com/css2?family=Alfa+Slab+One&family=Anton&family=Poppins:ital,wght@0,400;0,500;0,600;0,700;0,800;1,500&display=swap">
<style>
  :root{
    --page-bg:#c4c4c4;
    --sky-top:#1784d0;
    --sky-mid:#5fb4e4;
    --sky-light:#e4f1f7;
    --forest:#0b3d2a;
    --leaf:#19a35a;
    --band-top:#1ea462;
    --band-bottom:#0c7442;
    --mint:#22e57e;
    --sun:#f6e200;
    --white:#ffffff;
    --pin:#e5322d;
    --star:#f7a928;
  }
  *{margin:0;padding:0;box-sizing:border-box}
  html,body{width:1200px;height:874px;overflow:hidden;background:var(--page-bg)}
  .flyer{
    position:absolute;left:275px;top:17px;width:650px;height:840px;overflow:hidden;
    background:linear-gradient(180deg,var(--sky-top) 0%,var(--sky-mid) 25%,var(--sky-light) 55%,#eef5f4 66%);
    font-family:"Poppins",sans-serif;
  }
  .abs{position:absolute}
  .grass-photo{left:0;top:523px;width:460px;height:317px;
    background:linear-gradient(180deg,#3d6a3a 0%,#4f8a36 25%,#3f7a2a 60%,#27521c 100%)}
  .green-band{left:0;top:0;width:650px;height:840px}
  .title-golf{left:44px;top:26px;font-family:"Alfa Slab One",serif;font-size:118px;line-height:1;color:var(--white);letter-spacing:-2px}
  .title-tournament{left:44px;top:142px;font-family:"Alfa Slab One",serif;font-size:78px;line-height:1;color:var(--forest);letter-spacing:-1px}
  .title-balldrop{left:46px;top:218px;font-family:"Alfa Slab One",serif;font-size:45px;line-height:1;color:var(--forest)}
  .tournament-mark{left:492px;top:42px;display:flex;align-items:center;gap:6px}
  .tournament-mark .square{width:12px;height:12px;background:var(--sun)}
  .tournament-mark span{font-family:"Poppins",sans-serif;font-weight:700;font-size:15px;color:var(--white)}
  .helicopter-photo{left:262px;top:292px;width:130px;height:108px;border-radius:40% 30% 20% 30%;
    background:radial-gradient(ellipse at 40% 55%,#3a4150 0%,#6b7584 55%,rgba(180,195,210,0) 75%)}
  .prize-number{left:40px;top:318px;font-weight:700;font-size:142px;line-height:1;color:var(--forest)}
  .prize-week{left:93px;top:320px;font-size:27px;font-weight:600;color:var(--forest);line-height:1.1}
  .prize-family{left:93px;top:350px;font-size:31px;font-weight:700;color:var(--leaf);line-height:.92;letter-spacing:.5px}
  .prize-mexico{left:93px;top:412px;font-size:28px;font-weight:400;color:var(--forest);line-height:1}
  .rules{left:49px;top:465px;width:250px;font-size:12.3px;font-weight:600;line-height:14.6px;color:#111}
  .snapshot{background:var(--white);padding:7px;box-shadow:0 4px 10px rgba(0,0,0,.25)}
  .snapshot div{width:100%;height:100%}
  .snap-food{left:397px;top:238px;width:217px;height:157px;transform:rotate(3deg)}
  .snap-food div{background:linear-gradient(135deg,#2a1a12,#7a3a1c 45%,#c46a2a 70%,#3a2416)}
  .snap-pool{left:350px;top:391px;width:217px;height:136px;transform:rotate(-2deg)}
  .snap-pool div{background:linear-gradient(180deg,#c9a27f 0%,#3f9fd2 25%,#2a7fc0 100%)}
  .snap-beach{left:397px;top:514px;width:212px;height:149px;transform:rotate(3deg)}
  .snap-beach div{background:linear-gradient(180deg,#cfe0ea 0%,#9ec0d4 35%,#d9c6a6 60%,#e6d6bb 100%)}
  .enter-heading{left:47px;top:553px;font-size:24px;font-weight:800;line-height:.98;color:var(--sun)}
  .enter-detail{left:47px;top:607px;font-size:10.5px;font-weight:500;letter-spacing:1.6px;color:var(--white)}
  .date-month{left:42px;top:705px;transform:rotate(-90deg);transform-origin:left top;font-family:"Anton",sans-serif;font-size:34px;line-height:1;color:var(--white)}
  .date-day{left:83px;top:637px;width:70px;height:80px;background:var(--mint);
    font-family:"Anton",sans-serif;font-size:70px;line-height:80px;text-align:center;color:var(--forest)}
  .presence-note{left:171px;top:636px;font-size:10.5px;font-style:italic;font-weight:500;line-height:13px;color:var(--white)}
  .price-badge{left:313px;top:613px;width:100px;height:100px}
  .stay-intro{right:42px;top:684px;text-align:right;font-size:11.5px;font-weight:600;line-height:14px;color:var(--forest)}
  .resort-name{right:42px;top:715px;display:flex;align-items:center;gap:6px;font-family:"Alfa Slab One",serif;font-size:27px;line-height:1.1;color:var(--white)}
  .resort-rating{right:42px;top:754px;display:flex;align-items:center;gap:8px;font-size:9.5px;font-weight:600;letter-spacing:1px;color:var(--sun)}
  .school-name{left:290px;top:772px;width:100px;text-align:center;font-size:9px;font-weight:500;line-height:12px;color:var(--white)}
  .visit-label{left:408px;top:796px;font-size:10px;font-weight:500;letter-spacing:.8px;color:var(--white)}
  .web-band{left:470px;top:785px;width:180px;height:24px;background:var(--forest);
    clip-path:polygon(3% 10%,100% 0,100% 100%,0 92%,5% 55%)}
  .web-address{left:478px;top:789px;width:130px;text-align:right;font-size:11px;font-weight:700;letter-spacing:.6px;color:var(--white);white-space:nowrap}
</style>
</head>
<body>
<main class="flyer">
  <div class="abs grass-photo" role="img" aria-label="Close-up photo of a golf ball and club on green grass"></div>
  <svg class="abs green-band" viewBox="0 0 650 840" aria-hidden="true">
    <defs>
      <linearGradient id="bandFill" x1="0" y1="0" x2="0" y2="1">
        <stop offset="0" stop-color="#1ea462"/><stop offset="1" stop-color="#0c7442"/>
      </linearGradient>
    </defs>
    <polygon fill="url(#bandFill)" points="650,500 600,540 560,560 470,660 440,700 380,720 340,752 300,778 250,810 200,825 140,840 650,840"/>
  </svg>

  <h1 class="abs title-golf">Golf</h1>
  <div class="abs title-tournament">tournament</div>
  <div class="abs title-balldrop">Ball Drop</div>

  <div class="abs tournament-mark"><i class="square"></i><span>Meadow Classic</span></div>

  <div class="abs helicopter-photo" role="img" aria-label="Photo of a helicopter in flight"></div>

  <div class="abs prize-number">1</div>
  <div class="abs prize-week">week</div>
  <div class="abs prize-family">FAMILY<br>VACTION</div>
  <div class="abs prize-mexico">in MEXICO</div>

  <p class="abs rules">All golf balls will be dropped from helicopter and the ball that falls inside a hole wins the vacation.</p>

  <div class="abs snapshot snap-food"><div role="img" aria-label="Photo of food platters and drinks being toasted"></div></div>
  <div class="abs snapshot snap-pool"><div role="img" aria-label="Photo of kids playing with water toys in a pool"></div></div>
  <div class="abs snapshot snap-beach"><div role="img" aria-label="Photo of a family building a sandcastle on the beach"></div></div>

  <div class="abs enter-heading">TO ENTER<br>THE CONTEST</div>
  <div class="abs enter-detail">PURCHASE AS MANY GOLF BALLS FOR</div>

  <div class="abs date-month">NOV</div>
  <div class="abs date-day">11</div>
  <div class="abs presence-note">YOU DONT NEED<br>TO BE PRESENT<br>TO WIN...</div>

  <svg class="abs" style="left:270px;top:565px" width="110" height="70" viewBox="0 0 110 70" aria-hidden="true">
    <path d="M4 10 C30 0 60 6 52 30 C46 48 22 40 30 24 C38 10 66 18 80 40" fill="none" stroke="#e5322d" stroke-width="2.5" stroke-linecap="round"/>
    <path d="M72 38 L81 42 L82 32" fill="none" stroke="#e5322d" stroke-width="2.5" stroke-linecap="round" stroke-linejoin="round"/>
  </svg>
  <svg class="abs price-badge" viewBox="0 0 100 100" aria-label="$50">
    <polygon fill="#f6e200" points="50,4 57,15 69,8 72,21 85,19 83,32 96,36 88,47 97,57 85,63 89,76 76,77 74,90 62,86 55,97 47,88 36,96 31,84 18,87 19,74 6,70 13,59 4,49 14,41 8,29 21,27 21,14 34,16 38,4"/>
    <text x="50" y="62" text-anchor="middle" font-family="Poppins, sans-serif" font-weight="800" font-size="34" fill="#0b3d2a"><tspan font-size="18" dy="-12">$</tspan><tspan dy="12">50</tspan></text>
  </svg>

  <div class="abs stay-intro">THE WEEK<br>INCLUDES A STAY AT THE</div>
  <div class="abs resort-name">
    <svg width="14" height="20" viewBox="0 0 14 20" aria-hidden="true"><path d="M7 0C3 0 0 3 0 7c0 5 7 13 7 13s7-8 7-13c0-4-3-7-7-7z" fill="#e5322d"/><circle cx="7" cy="7" r="2.6" fill="#fff"/></svg>
    Calloway Resort
  </div>
  <div class="abs resort-rating">A 5 STAR HOTEL
    <svg width="100" height="16" viewBox="0 0 100 16" aria-label="5 stars">
      <g fill="#f7a928">
        <polygon points="8,0 10.4,5.3 16,5.8 11.8,9.6 13,15.2 8,12.3 3,15.2 4.2,9.6 0,5.8 5.6,5.3"/>
        <polygon transform="translate(21 0)" points="8,0 10.4,5.3 16,5.8 11.8,9.6 13,15.2 8,12.3 3,15.2 4.2,9.6 0,5.8 5.6,5.3"/>
        <polygon transform="translate(42 0)" points="8,0 10.4,5.3 16,5.8 11.8,9.6 13,15.2 8,12.3 3,15.2 4.2,9.6 0,5.8 5.6,5.3"/>
        <polygon transform="translate(63 0)" points="8,0 10.4,5.3 16,5.8 11.8,9.6 13,15.2 8,12.3 3,15.2 4.2,9.6 0,5.8 5.6,5.3"/>
        <polygon transform="translate(84 0)" points="8,0 10.4,5.3 16,5.8 11.8,9.6 13,15.2 8,12.3 3,15.2 4.2,9.6 0,5.8 5.6,5.3"/>
      </g>
    </svg>
  </div>

  <div class="abs school-name">Holy Meadow Of Brenton Catholic School</div>

  <div class="abs visit-label">visit us at</div>
  <div class="abs web-band"></div>
  <div class="abs web-address">www.hmbrenton.org</div>
</main>
</body>
</html>
```